Business card design for strategy and management consulting company. Would like to have a clean and professional business card, based on the attached logo. The company is a strategy and management consulting company focusing on sustainable business modlels based on economic, social and environmental market opportunities. Preferably the logo should be included on both sides of the design.

Industry/Entity Type

Business

Contact Information for Business Card

Håvard Lilleby, CEO/Management consultant
havard.lilleby@quarvenpartners.example
Mob: +47 948 26 317
Office: Vikfjell gate 14, pb 312 sentrum, N-0172 Oslo Norway

Requirements
Must have
• Include attached logo
Nice to have
• Would like to have the logo on both sides
Should not have
• Many colours.

```html
<!DOCTYPE html>
<html lang="en">
<head>
<meta charset="utf-8">
<title>Quarven – Business Card</title>
<link href="https://fonts.googleapis.com/css2?family=Open+Sans:wght@400;600&display=swap" rel="stylesheet">
<style>
  :root {
    --page: #ffffff;
    --card: #000000;
    --ink: #ffffff;
    --accent: #f7e017;
    --rule: #ffffff;
  }
  * { box-sizing: border-box; margin: 0; padding: 0; }
  html, body {
    width: 1200px; height: 1200px; overflow: hidden;
    background: var(--page);
    font-family: "Open Sans", Arial, sans-serif;
  }
  .sheet { position: relative; width: 1200px; height: 1200px; }
  .card {
    position: absolute; top: 477px;
    width: 432px; height: 246px;
    background: var(--card); color: var(--ink); overflow: hidden;
  }
  .card--front { left: 130px; }
  .card--back { left: 610px; }

  .wordmark {
    position: absolute; font-weight: 600; color: var(--ink);
    letter-spacing: -0.5px; line-height: 1;
  }
  .card--front .wordmark { left: 26px; top: 22px; font-size: 27px; }
  .card--back .wordmark {
    left: 0; right: 0; top: 84px; text-align: center; font-size: 76px;
  }
  .brand-dot {
    position: absolute; border-radius: 50%; background: var(--accent);
  }
  .card--back .brand-dot { width: 16px; height: 16px; left: 372px; top: 74px; }

  .accent-disc {
    position: absolute; left: 24px; top: 90px;
    width: 120px; height: 120px; border-radius: 50%; background: var(--accent);
  }
  .divider {
    position: absolute; left: 164px; top: 16px;
    width: 1.5px; height: 216px; background: var(--rule);
  }
  .person { position: absolute; left: 174px; top: 20px; }
  .person__name { font-size: 17px; font-weight: 400; letter-spacing: 0.4px; line-height: 1.2; }
  .person__title { font-size: 11.5px; line-height: 1.4; }

  .contact { position: absolute; left: 174px; right: 12px; top: 138px; list-style: none; }
  .contact__row {
    display: flex; align-items: flex-start; gap: 7px;
    font-size: 10.5px; line-height: 17px; margin-bottom: 2px;
  }
  .contact__row span { white-space: nowrap; }
  .contact__icon { width: 14px; height: 17px; flex: none; fill: var(--ink); }
</style>
</head>
<body>
<main class="sheet">
  <section class="card card--front" aria-label="Card front">
    <div class="wordmark">Quarven</div>
    <div class="accent-disc"></div>
    <div class="divider"></div>
    <div class="person">
      <p class="person__name">HÅVARD LILLEBY</p>
      <p class="person__title">CEO/Management consultant</p>
    </div>
    <ul class="contact">
      <li class="contact__row">
        <svg class="contact__icon" viewBox="0 0 16 19" aria-hidden="true"><path d="M1 5h14v9H1z M1 5l7 5 7-5" fill="none" stroke="#fff" stroke-width="1.6"/></svg>
        <span>havard.lilleby@quarvenpartners.example</span>
      </li>
      <li class="contact__row">
        <svg class="contact__icon" viewBox="0 0 16 19" aria-hidden="true"><rect x="3.5" y="2.5" width="9" height="14" rx="1.5" fill="none" stroke="#fff" stroke-width="1.6"/><rect x="6" y="13" width="4" height="1.4"/></svg>
        <span>+47 948 26 317</span>
      </li>
      <li class="contact__row">
        <svg class="contact__icon" viewBox="0 0 16 19" aria-hidden="true"><path d="M8 2 0.5 9h2.3v7h4v-4.5h2.4V16h4V9h2.3z"/></svg>
        <span>Vikfjell gate 14,<br>pb 312 sentrum, N-0172 Oslo,<br>Norway</span>
      </li>
    </ul>
  </section>

  <section class="card card--back" aria-label="Card back">
    <div class="wordmark">Quarven</div>
    <div class="brand-dot"></div>
  </section>
</main>
</body>
</html>
```